" O nome Valtessora significa dentro do movimento. A clínica tem como carro chefe um trabalho chamado de videoanálise de movimento. Usamos um software para realizar análise de marcha, corrida, salto, estabilidade, flexibilidade entre outros. Identificamos alteraçoes no movimento que possam ser a causa de dor ou diminmuiçao no rendimento físico-funcional. Alteraçoes identificadas entramos com a reabilitaçao usando Pilates, RPG, Hidroterapia, Treinamento Funcional, Osteopatia entre outros. Nosso foco: resultados! "

```html
<!DOCTYPE html>
<html lang="pt-BR">
<head>
<meta charset="utf-8">
<title>Valtessora — Cartão de Visita</title>
<link rel="stylesheet" href="https://fonts.googleapis.com/css2?family=PT+Sans:wght@400;700&display=swap">
<style>
  :root {
    --bg: #e9eaec;
    --card: #ffffff;
    --brand-blue: #2b4f9e;
    --soft-blue: #6f8fcf;
    --soft-grey: #b9bcc1;
    --text-grey: #555759;
  }
  * { margin: 0; padding: 0; box-sizing: border-box; }
  html, body {
    width: 1200px; height: 1200px; overflow: hidden;
    background: var(--bg);
    font-family: "PT Sans", sans-serif;
  }
  .canvas { position: relative; width: 1200px; height: 1200px; }
  .card {
    position: absolute;
    width: 876px; height: 504px;
    background: var(--card);
    overflow: hidden;
  }
  .card--front { left: 91px; top: 60px; }
  .card--back { left: 247px; top: 612px; }

  .brand {
    position: absolute; left: 0; right: 0; top: 170px;
    display: flex; flex-direction: column; align-items: center;
  }
  .brand__dot {
    width: 70px; height: 70px; border-radius: 50%;
    background: var(--brand-blue);
    margin-bottom: 14px;
  }
  .brand__name {
    font-weight: 700; font-size: 76px; line-height: 1;
    color: var(--brand-blue); letter-spacing: -1px;
  }
  .brand__tagline {
    margin-top: 8px;
    font-size: 17px; letter-spacing: 2.5px;
    color: var(--brand-blue);
  }

  .back-mark {
    position: absolute; left: -10px; top: 84px;
    width: 336px; height: 336px;
  }
  .person {
    position: absolute; left: 487px; top: 98px;
    font-size: 27px; color: var(--text-grey);
  }
  .contact {
    position: absolute; left: 487px; top: 296px;
    list-style: none;
    font-size: 20px; line-height: 24px; color: var(--text-grey);
  }
</style>
</head>
<body>
<main class="canvas">
  <section class="card card--front">
    <div class="brand">
      <span class="brand__dot"></span>
      <h1 class="brand__name">Valtessora</h1>
      <p class="brand__tagline">Clínica da Performance Humana</p>
    </div>
  </section>

  <section class="card card--back">
    <svg class="back-mark" viewBox="0 0 336 336" role="img" aria-label="Elemento decorativo da marca">
      <defs>
        <linearGradient id="markFill" x1="0" y1="0" x2="0" y2="1">
          <stop offset="0" stop-color="#6f8fcf"/>
          <stop offset="1" stop-color="#b9bcc1"/>
        </linearGradient>
      </defs>
      <circle cx="168" cy="168" r="168" fill="url(#markFill)"/>
    </svg>
    <p class="person">Nome Sobrenome</p>
    <ul class="contact">
      <li>Endereço &nbsp;Onono non nono, 999</li>
      <li>Cep: 99999-99 - Nononono- NO</li>
      <li>Fone: (99) 9999-9999</li>
      <li>contato@valtessora.com</li>
      <li>www.valtessora.com</li>
    </ul>
  </section>
</main>
</body>
</html>
```